KEM Logistics - Banner 2.5' x 8' for 20+ locations

Need a banner designed that will pop. This banner will be displayed at over 20 of our transportation facilities. Goal is for the banner to grab the attention of employees, contractors and clients and help reinforce our mission and core values. Designed needs to include KEM Logo, our core values and mission statement. Red and Black are the main company colors and we need to stay within that theme and color pallet. Attached is a previous version that was too basic and boring. Willing to consider a design that excludes the mission statement.

```html
<!DOCTYPE html>
<html lang="en">
<head>
<meta charset="utf-8">
<title>KEM Logistics – Core Values Banner</title>
<link rel="stylesheet" href="https://fonts.googleapis.com/css2?family=Oswald:wght@500;600&family=Open+Sans:wght@700&family=Roboto:ital,wght@0,400;1,400&display=swap">
<style>
  :root {
    --backdrop: #e6e6e6;
    --banner: #f6f6f6;
    --red-bright: #d9262a;
    --red-mid: #b01e25;
    --red-deep: #961c22;
    --red-dark: #8c1a20;
    --charcoal: #2d2a27;
    --white: #ffffff;
  }
  * { margin: 0; padding: 0; box-sizing: border-box; }
  html, body {
    width: 1200px;
    height: 515px;
    overflow: hidden;
    background: var(--backdrop);
  }
  .banner {
    position: absolute;
    left: 95px;
    top: 100px;
    width: 1005px;
    height: 313px;
    background: linear-gradient(90deg, var(--white) 0%, var(--banner) 100%);
  }
  .value {
    position: absolute;
    height: 44px;
    display: flex;
    align-items: center;
    justify-content: center;
    color: var(--white);
    white-space: nowrap;
    overflow: hidden;
  }
  .value--caps {
    font-family: "Oswald", "Arial Narrow", sans-serif;
    font-weight: 500;
    font-size: 18px;
    letter-spacing: 0.7px;
    text-transform: uppercase;
  }
  .value--bold {
    font-family: "Open Sans", Arial, sans-serif;
    font-weight: 700;
    font-size: 18px;
  }
  .value--plain {
    font-family: "Roboto", Arial, sans-serif;
    font-weight: 400;
    font-size: 20px;
  }
  .value--large { font-size: 24px; }
  .bg-bright { background: var(--red-bright); }
  .bg-mid { background: var(--red-mid); }
  .bg-deep { background: var(--red-deep); }
  .bg-dark { background: var(--red-dark); }

  .mission {
    position: absolute;
    left: 20px;
    top: 175px;
    width: 705px;
    height: 121px;
    background: var(--charcoal);
    color: var(--white);
  }
  .mission__mark {
    position: absolute;
    left: 33px;
    top: 37px;
    width: 66px;
    height: 46px;
  }
  .mission__text {
    position: absolute;
    left: 132px;
    top: 20px;
    width: 560px;
    font-family: "Roboto", Arial, sans-serif;
    font-style: italic;
    font-size: 19px;
    line-height: 27px;
    letter-spacing: 0.3px;
  }
  .brand {
    position: absolute;
    left: 745px;
    top: 125px;
    width: 240px;
    text-align: center;
    font-family: "Oswald", "Arial Narrow", sans-serif;
    font-weight: 600;
    font-size: 42px;
    line-height: 60px;
    color: var(--red-bright);
  }
</style>
</head>
<body>
  <main class="banner">
    <div class="value value--caps bg-bright" style="left:20px;top:19px;width:400px;">Do the right things for the right reasons</div>
    <div class="value value--plain bg-deep" style="left:426px;top:19px;width:299px;">Deliver WOW through service</div>

    <div class="value value--bold bg-mid" style="left:20px;top:71px;width:355px;">Build a positive Team atmosphere</div>
    <div class="value value--caps bg-dark" style="left:383px;top:71px;width:342px;">Pursue growth and development</div>

    <div class="value value--plain bg-deep" style="left:20px;top:123px;width:331px;">Build a positive Team atmosphere</div>
    <div class="value value--bold bg-bright" style="left:357px;top:123px;width:224px;">Do everything safely</div>
    <div class="value value--caps value--large bg-mid" style="left:588px;top:123px;width:137px;">Have fun</div>

    <section class="mission">
      <svg class="mission__mark" viewBox="0 0 66 54" preserveAspectRatio="none" aria-hidden="true">
        <path fill="#ffffff" d="M0 54V28C0 12 8 3 22 0l3 8c-7 3-10 8-10 16h12v30zM38 54V28C38 12 46 3 60 0l3 8c-7 3-10 8-10 16h12v30z"/>
      </svg>
      <p class="mission__text">Provide the best customer experience while creating an environment of growth and opportunity for our customers, employees, and service providers.</p>
    </section>

    <div class="brand">KEM Logistics</div>
  </main>
</body>
</html>
```